Carrowfield Hotel

A Hotel (Pub) in Sydney CBD. Posters will be outside of Hotel informing People what is on in Hotel.
We will be Printing in A1 size.
CARROWFIELD HOTEL
Open 9am - 3am 7 Days
Monday - Thursday
Happy Hour
4pm - 6pm
Local Beer & Wine
Wednesday
Poker Night: Great $$$ Prizes
Everyday
Steak or Schniztels: Served with Mashed Potato & Salad or Chips & Salad - $8.50
Live Sport on the Big Screen
BISTRO
OPEN 7 DAYS 12- 9pm
Daily Blackboard Specials + Full Menu Inside
Best service in Town
Target Market(s)
Male or Female 18 to Seniors.Passing Trade.
Industry/Entity Type
Hotel
Look and feel
Each slider illustrates characteristics of the customer's brand and the style your logo design should communicate.

```html
<!DOCTYPE html>
<html lang="en">
<head>
<meta charset="utf-8">
<title>Carrowfield Hotel – What's On</title>
<link href="https://fonts.googleapis.com/css2?family=Limelight&family=Alfa+Slab+One&family=Creepster&family=Fredoka:wght@600;700&display=swap" rel="stylesheet">
<style>
  :root {
    --ink: #050303;
    --blood: #7a0c0e;
    --blood-deep: #3c0506;
    --title-red: #c4161c;
    --band: #1b1b1d;
    --teal: #2f6e6a;
    --sport-red: #b3151a;
    --white: #ffffff;
    --photo-warm: #6b5a2a;
    --photo-dark: #2a2212;
  }
  * { margin: 0; padding: 0; box-sizing: border-box; }
  html, body { width: 960px; height: 1200px; overflow: hidden; background: var(--ink); }
  .poster {
    position: relative;
    width: 960px;
    height: 1200px;
    overflow: hidden;
    background:
      radial-gradient(ellipse 420px 260px at 120px 80px, var(--blood) 0%, transparent 70%),
      radial-gradient(ellipse 380px 220px at 860px 60px, var(--blood-deep) 0%, transparent 75%),
      radial-gradient(ellipse 480px 320px at 820px 430px, var(--blood) 0%, transparent 70%),
      radial-gradient(ellipse 360px 260px at 150px 640px, var(--blood-deep) 0%, transparent 75%),
      radial-gradient(ellipse 300px 200px at 60px 1150px, var(--blood) 0%, transparent 70%),
      radial-gradient(ellipse 360px 260px at 920px 1120px, var(--blood) 0%, transparent 70%),
      var(--ink);
  }
  .artwork { position: absolute; inset: 0; }
  .venue-photo {
    position: absolute;
    left: 125px; top: 640px;
    width: 835px; height: 560px;
    background:
      radial-gradient(ellipse 420px 300px at 45% 55%, var(--photo-warm) 0%, var(--photo-dark) 60%, transparent 100%);
    opacity: 0.85;
  }
  .headline {
    position: absolute; left: 0; width: 960px; top: 698px;
    text-align: center;
    font-family: "Fredoka", sans-serif; font-weight: 700;
    font-size: 76px; color: var(--white); letter-spacing: 0.5px;
    text-shadow: 0 0 2px #000, 2px 3px 6px rgba(0,0,0,0.8);
  }
  .whats-on {
    position: absolute; left: 20px; top: 780px;
    font-family: Arial, Helvetica, sans-serif;
    font-size: 31px; color: var(--white); line-height: 1;
  }
  .whats-on p { position: absolute; left: 0; white-space: nowrap; }
  .bistro {
    position: absolute; left: 598px; top: 788px;
    font-family: "Fredoka", sans-serif; font-weight: 600;
    color: var(--white); line-height: 1;
  }
  .bistro p { position: absolute; left: 0; white-space: nowrap; }
  .bistro .bistro-title { top: 0; font-size: 31px; }
  .bistro .bistro-line { font-size: 24px; }
</style>
</head>
<body>
<main class="poster">
  <div class="venue-photo" role="img" aria-label="Faded photo of playing cards and the hotel building on a city street corner at dusk"></div>

  <svg class="artwork" width="960" height="1200" viewBox="0 0 960 1200">
    <polygon class="feature-band" points="0,355 960,77 960,288 0,586" fill="var(--band)" opacity="0.92"/>

    <text class="hotel-name" x="28" y="78" textLength="905" lengthAdjust="spacingAndGlyphs"
          font-family="Limelight, serif" font-size="72" fill="var(--white)"
          stroke="var(--title-red)" stroke-width="3" paint-order="stroke">CARROWFIELD HOTEL</text>
    <text class="opening-hours" x="232" y="126" textLength="432" lengthAdjust="spacingAndGlyphs"
          font-family="'Alfa Slab One', serif" font-size="30" fill="var(--white)">Open 9am - 3am 7 Days</text>

    <rect class="photo-friends" x="20" y="425" width="105" height="95" fill="#5a4a3e" transform="rotate(-6 72 472)" role="img" aria-label="Photo of friends out together at the pub"/>
    <rect class="photo-food" x="374" y="282" width="160" height="105" fill="#8a6a3a" transform="rotate(-14 454 334)" role="img" aria-label="Photo of a burger with chips"/>
    <rect class="photo-drinks" x="712" y="160" width="58" height="152" rx="14" fill="#4f5a2c" transform="rotate(-8 741 236)" role="img" aria-label="Photo of a bottle of beer"/>

    <text class="feature-word" x="192" y="415" font-family="'Alfa Slab One', serif" font-size="33" fill="var(--teal)">Friends</text>
    <text class="feature-word" x="552" y="302" font-family="'Alfa Slab One', serif" font-size="33" fill="var(--teal)">Food</text>
    <text class="feature-word" x="803" y="216" font-family="'Alfa Slab One', serif" font-size="33" fill="var(--teal)">Drinks</text>

    <text class="live-sport" x="118" y="592" textLength="830" lengthAdjust="spacingAndGlyphs"
          transform="rotate(-19.5 118 592)"
          font-family="Creepster, cursive" font-size="58" fill="var(--sport-red)">LIVE SPORT ON THE BIG SCREEN</text>
  </svg>

  <h1 class="headline">Best service in Town</h1>

  <section class="whats-on">
    <p style="top:0">Monday - Thursday</p>
    <p style="top:36px">Happy Hour</p>
    <p style="top:68px">4pm - 6pm</p>
    <p style="top:102px">Local Beer &amp; Wine</p>
    <p style="top:174px">Wednesday</p>
    <p style="top:217px">Poker Night: Great $$$ Prizes</p>
    <p style="top:261px">Everyday</p>
    <p style="top:309px">Steak or Schniztels: Served with Mashed Potato &amp;</p>
    <p style="top:364px">Salad or Chips &amp; Salad - $8.50</p>
  </section>

  <section class="bistro">
    <p class="bistro-title">BISTRO</p>
    <p class="bistro-line" style="top:70px">OPEN 7 DAYS 12- 9pm</p>
    <p class="bistro-line" style="top:106px">Daily Blackboard Specials</p>
    <p class="bistro-line" style="top:146px">+ Full Menu Inside</p>
  </section>
</main>
</body>
</html>
```